Bref créative
BRFinishing Co.
NYC | Westchester |
Simple
Darrel Hutchins Jr
Project Manager
8 Lowell Terrace
Cold Meadow, NY 10488
brfinishinginfo@brfmail-example.com
We'd like to see ideas for vertical card designs as well.
It's all in the finish
Logo
logo

```html
<!DOCTYPE html>
<html lang="en">
<head>
<meta charset="utf-8">
<title>BRFinishing Co. – Business Card</title>
<link rel="stylesheet" href="https://fonts.googleapis.com/css2?family=Arimo:wght@400;700&display=swap">
<style>
  :root {
    --page-bg: #ffffff;
    --card-edge: #c9c9c9;
    --card-light: #ffffff;
    --card-shade: #e4e4e4;
    --ink: #2b2b2b;
    --ink-soft: #3a3a3a;
    --brand-mark: #8a8a8a;
    --band-light: #b8b8b8;
    --band-dark: #4a4a4a;
  }
  * { margin: 0; padding: 0; box-sizing: border-box; }
  html, body {
    width: 1200px;
    height: 1002px;
    overflow: hidden;
    background: var(--page-bg);
    font-family: "Arimo", Arial, sans-serif;
    color: var(--ink);
  }
  .sheet { position: relative; width: 1200px; height: 1002px; }
  .card {
    position: absolute;
    top: 8px;
    height: 986px;
    border: 2px solid var(--card-edge);
    background: radial-gradient(ellipse at 50% 45%, var(--card-light) 0%, #f6f6f6 55%, var(--card-shade) 100%);
    overflow: hidden;
  }
  .card--front { left: 14px; width: 572px; }
  .card--back { left: 628px; width: 564px; }

  .brand {
    position: absolute;
    display: flex;
    align-items: center;
    gap: 14px;
  }
  .brand__mark {
    width: 30px; height: 30px;
    background: var(--brand-mark);
    flex: none;
  }
  .brand__name {
    font-weight: 400;
    font-size: 40px;
    color: var(--ink);
    white-space: nowrap;
  }
  .card--front .brand { left: 26px; top: 90px; }
  .card--back .brand { left: 30px; top: 506px; }

  .person {
    position: absolute;
    top: 440px;
    left: 0; right: 0;
    text-align: center;
  }
  .person__name { font-weight: 700; font-size: 28px; color: var(--ink); }
  .person__role { font-size: 27px; margin-top: 8px; color: var(--ink-soft); }

  .contact {
    position: absolute;
    left: 12px;
    top: 785px;
    font-size: 23px;
    line-height: 28px;
    color: var(--ink-soft);
    list-style: none;
  }

  .footer-band {
    position: absolute;
    left: 0; right: 0;
    bottom: 22px;
    height: 34px;
    background: linear-gradient(to bottom, var(--band-light) 0%, var(--band-light) 22%, #fff 24%, #fff 30%, #8c8c8c 32%, var(--band-dark) 70%, #6a6a6a 100%);
  }
</style>
</head>
<body>
<div class="sheet">
  <section class="card card--front" aria-label="Card front">
    <div class="brand">
      <span class="brand__mark"></span>
      <span class="brand__name">BRFinishing Co.</span>
    </div>
    <div class="person">
      <p class="person__name">Darrel Hutchins Jr</p>
      <p class="person__role">Project Manager</p>
    </div>
    <ul class="contact">
      <li>8 Lowell Terrace</li>
      <li>Cold Meadow, NY 10488</li>
      <li>Phone : 555.013.2290</li>
      <li>Email : brfinishinginfo@brfmail-example.com</li>
    </ul>
    <div class="footer-band"></div>
  </section>

  <section class="card card--back" aria-label="Card back">
    <div class="brand">
      <span class="brand__mark"></span>
      <span class="brand__name">BRFinishing Co.</span>
    </div>
  </section>
</div>
</body>
</html>
```